***Design a Nutritional Supplement Label for Bright Harvest!***

I have an existing label, I want to keep the logo but change the rest of the design. I am open to different creative ideas, but it needs to look appropriate for the shelves at Bright Harvest. This means it needs to look professional and premium, without being sterile and boring. I feel like my current label looks a little 1990s. You can play with the colors, font and design elements, while keeping the logo, descriptive text and the same layout. Feel free to take some bold chances. (You cannot change the font in the supplement facts section)

Font styles to use
Sans Serif

Colors

Designer to choose colors to be used in the design.

Requirements
Must have
• Keep the same text and layout. Keep the "Muscle Haven" logo as-is. DO NOT CHANGE THE LOGO!!

```html
<!DOCTYPE html>
<html lang="en">
<head>
<meta charset="utf-8">
<title>Muscle Haven Supplement Label</title>
<link rel="stylesheet" href="https://fonts.googleapis.com/css2?family=Montserrat:wght@700&family=Nunito:wght@700;800&display=swap">
<style>
  :root {
    --backdrop: #2b6793;
    --label-top: #cfe0ee;
    --label-bottom: #e6eef6;
    --brand-blue: #1a86cf;
    --wave-deep: #2f6fb8;
    --wave-light: #a9cdea;
    --ink: #3c3f44;
    --ring: #4a4d52;
  }
  * { margin: 0; padding: 0; box-sizing: border-box; }
  html, body {
    width: 1200px;
    height: 675px;
    overflow: hidden;
    background: var(--backdrop);
  }
  .canvas {
    position: relative;
    width: 1200px;
    height: 675px;
    background: var(--backdrop);
  }
  .label {
    position: absolute;
    left: 380px;
    top: 106px;
    width: 440px;
    height: 462px;
    background: linear-gradient(180deg, var(--label-top) 0%, var(--label-bottom) 100%);
    overflow: hidden;
  }
  .brand-name {
    position: absolute;
    left: 0;
    top: 78px;
    width: 100%;
    text-align: center;
    font-family: "Montserrat", sans-serif;
    font-weight: 700;
    font-size: 46px;
    letter-spacing: 1px;
    color: var(--brand-blue);
  }
  .wave-band {
    position: absolute;
    left: 0;
    top: 180px;
    width: 100%;
    height: 130px;
    background: linear-gradient(180deg,
      rgba(169, 205, 234, 0) 0%,
      var(--wave-light) 25%,
      var(--wave-deep) 45%,
      var(--wave-light) 70%,
      rgba(169, 205, 234, 0) 100%);
    opacity: 0.75;
  }
  .claims {
    position: absolute;
    left: 98px;
    top: 272px;
  }
  .claim-text {
    font-family: "Nunito", sans-serif;
    font-weight: 800;
    font-size: 20px;
    fill: var(--ink);
  }
  .count-pill {
    position: absolute;
    left: 140px;
    top: 392px;
    width: 156px;
    height: 46px;
    border: 1.5px solid var(--ring);
    border-radius: 23px;
    text-align: center;
    font-family: "Nunito", sans-serif;
    color: var(--ink);
    padding-top: 3px;
  }
  .count-pill .count {
    display: block;
    font-weight: 800;
    font-size: 18px;
    line-height: 22px;
  }
  .count-pill .type {
    display: block;
    font-weight: 800;
    font-size: 10.5px;
    line-height: 14px;
  }
</style>
</head>
<body>
  <main class="canvas">
    <section class="label">
      <h1 class="brand-name">Muscle Haven</h1>
      <div class="wave-band" role="img" aria-label="Flowing blue wave pattern"></div>
      <svg class="claims" width="244" height="124" viewBox="0 0 244 124">
        <circle cx="62" cy="62" r="60" fill="none" stroke="var(--ring)" stroke-width="1.5"/>
        <circle cx="182" cy="62" r="60" fill="none" stroke="var(--ring)" stroke-width="1.5"/>
        <text class="claim-text" x="62" y="57" text-anchor="middle">High</text>
        <text class="claim-text" x="62" y="81" text-anchor="middle">Absorption</text>
        <text class="claim-text" x="182" y="56" text-anchor="middle">Fast</text>
        <text class="claim-text" x="182" y="80" text-anchor="middle">Acting</text>
      </svg>
      <div class="count-pill">
        <span class="count">180 CAPSULES</span>
        <span class="type">DIETARY SUPPLEMENT</span>
      </div>
    </section>
  </main>
</body>
</html>
```